Coastal Bright Sweep Business Card

We are a cleaning and waste management company with the slogan "making waste to landfill a thing of the past". We would like a re-design of our current business card. On the front we want to continue to use our logo as the focus point. On the back, we want the whole thing re-done to be less busy. We want the staff member’s name, the job title, mobile number, email and website. We do not want the address on the card. We still want the green, black and blue colours used, but a new font for the information on the back. Please do not change the logo design at all. We are also thinking about using icons to replace the text ‘mobile, email, website’. The “events + commercial” banner needs to be incorporated somewhere and needs to read “events + commercial + waste”. Another important point for consideration is that we are very concerned about being environmentally sustainable and will be printing on recycled paper. All designs should be made to compliment this in regards to boldness and colouring. Please find attached our logo, our colour chart and an image of our current business card.

```html
<!DOCTYPE html>
<html lang="en">
<head>
<meta charset="utf-8">
<title>Coastal Bright Sweep Business Card</title>
<link rel="stylesheet" href="https://fonts.googleapis.com/css2?family=Lato:ital,wght@0,400;0,700;0,900;1,700&display=swap">
<style>
  :root {
    --backdrop: #3a3a3a;
    --paper: #efede8;
    --navy: #1a3e78;
    --green: #7dc242;
    --blue: #00a8e8;
    --ink: #1c1c1c;
    --white: #ffffff;
  }
  * { box-sizing: border-box; margin: 0; padding: 0; }
  html, body {
    width: 1200px; height: 900px; overflow: hidden;
    background: var(--backdrop);
    font-family: "Lato", sans-serif;
  }
  .canvas {
    position: relative; width: 1200px; height: 900px;
  }
  .card {
    position: absolute; left: 280px;
    width: 640px; height: 392px;
    background: var(--paper);
    box-shadow: 0 10px 30px rgba(0,0,0,0.45);
    overflow: hidden;
  }
  .card--front { top: 40px; }
  .card--back { top: 468px; }

  /* brand name block */
  .brand-name {
    font-family: "Lato", sans-serif;
    font-weight: 900;
    color: var(--navy);
    text-transform: uppercase;
    line-height: 1.02;
    letter-spacing: 0.04em;
    text-align: center;
    display: flex; flex-direction: column; align-items: center;
  }
  .brand-mark {
    width: 22px; height: 22px; border-radius: 50%;
    background: var(--blue); margin-bottom: 12px;
  }
  .card--front .brand-name {
    position: absolute; left: 0; right: 0; top: 70px;
    font-size: 52px;
  }
  .front-url {
    position: absolute; left: 0; right: 0; top: 318px;
    text-align: center; font-size: 18px; color: var(--ink);
  }

  /* back side */
  .accent-tab {
    position: absolute; left: 0; top: 44px;
    width: 14px; height: 50px; background: var(--blue);
  }
  .staff-name {
    position: absolute; left: 40px; top: 44px;
    font-size: 26px; font-weight: 700; font-style: italic;
    color: var(--blue);
  }
  .staff-role {
    position: absolute; left: 40px; top: 78px;
    font-size: 16px; color: var(--ink);
  }
  .contact-list {
    position: absolute; left: 40px; top: 150px;
    list-style: none;
  }
  .contact-item {
    display: flex; align-items: center; gap: 10px;
    font-size: 16px; color: var(--ink); height: 26px;
  }
  .contact-icon { width: 14px; height: 14px; flex: none; }
  .card--back .brand-name {
    position: absolute; left: 340px; width: 280px; top: 70px;
    font-size: 34px;
  }
  .bands { position: absolute; left: 0; top: 0; }
  .tagline {
    position: absolute; left: 20px; top: 293px;
    font-size: 17px; color: var(--white); letter-spacing: 0.02em;
    text-transform: uppercase;
  }
</style>
</head>
<body>
<main class="canvas">

  <section class="card card--front" aria-label="Card front">
    <div class="brand-name">
      <span class="brand-mark"></span>
      <span>Coastal</span><span>Bright</span><span>Sweep</span>
    </div>
    <p class="front-url">www.coastalbrightsweep.com.au</p>
  </section>

  <section class="card card--back" aria-label="Card back">
    <svg class="bands" width="640" height="392" viewBox="0 0 640 392" aria-hidden="true">
      <polygon points="0,288 336,288 318,318 0,318" fill="var(--green)"/>
      <polygon points="326,318 640,318 640,342 312,342" fill="var(--blue)"/>
    </svg>

    <span class="accent-tab"></span>
    <h1 class="staff-name">Morgan Ellery</h1>
    <p class="staff-role">Client Manager</p>

    <ul class="contact-list">
      <li class="contact-item">
        <svg class="contact-icon" viewBox="0 0 14 14" aria-label="Mobile"><rect x="3.5" y="0.5" width="7" height="13" rx="1.5" fill="none" stroke="var(--blue)" stroke-width="1.4"/><circle cx="7" cy="11" r="0.9" fill="var(--blue)"/></svg>
        <span>0400 555 218</span>
      </li>
      <li class="contact-item">
        <svg class="contact-icon" viewBox="0 0 14 14" aria-label="Email"><rect x="0.5" y="2.5" width="13" height="9" fill="var(--blue)"/><polyline points="0.5,2.5 7,8 13.5,2.5" fill="none" stroke="var(--paper)" stroke-width="1.2"/></svg>
        <span>mellery@coastalbrightsweep.com.au</span>
      </li>
      <li class="contact-item">
        <svg class="contact-icon" viewBox="0 0 14 14" aria-label="Website"><circle cx="7" cy="7" r="6" fill="var(--blue)"/><path d="M1 7h12M7 1c-3 3-3 9 0 12M7 1c3 3 3 9 0 12" fill="none" stroke="var(--paper)" stroke-width="1"/></svg>
        <span>www.coastalbrightsweep.com.au</span>
      </li>
    </ul>

    <p class="tagline">Events + Commercial + Waste</p>

    <div class="brand-name">
      <span class="brand-mark"></span>
      <span>Coastal</span><span>Bright</span><span>Sweep</span>
    </div>
  </section>

</main>
</body>
</html>
```